plumbing & gas fitting business card design

We need a business card design for a plumbing & gas fitting company. The company covers commercial, domestic and maintenance work. We would like a modern design communicating efficiency and sophistication. preferred colours would include (red grey & black) or (green grey & black). Please DO NOT include any water droplets.

Industry/Entity Type

Business

Contact Information for Business Card

Vortig Plumbing & Gas, Commercial Domestic & Maintenance, licence no. 617394K, ABN 47215830962, Phone 0417382956, Email vortigplumbingandgas@corvanet.com

```html
<!DOCTYPE html>
<html lang="en">
<head>
<meta charset="utf-8">
<title>Vortig Plumbing &amp; Gas – Business Card Options</title>
<link rel="stylesheet" href="https://fonts.googleapis.com/css2?family=Montserrat:wght@600&display=swap">
<style>
  :root {
    --page: #ffffff;
    --card: #ffffff;
    --card-border: #d4d4d4;
    --ink: #231f20;
    --green: #8dc63f;
    --red: #c1202d;
    --silver-light: #f2f2f2;
    --silver-mid: #b5b5b5;
    --silver-dark: #6f6f6f;
  }
  * { box-sizing: border-box; margin: 0; padding: 0; }
  html, body {
    width: 1200px;
    height: 768px;
    overflow: hidden;
    background: var(--page);
  }
  .sheet {
    position: relative;
    width: 1200px;
    height: 768px;
  }
  .card {
    position: absolute;
    width: 580px;
    height: 352px;
    background: var(--card);
    border: 1px solid var(--card-border);
    overflow: hidden;
  }
  .card--top-left { left: 7px; top: 7px; }
  .card--top-right { left: 610px; top: 7px; }
  .card--bottom-left { left: 7px; top: 407px; }
  .card--bottom-right { left: 610px; top: 407px; }

  .card--green { --accent: var(--green); }
  .card--red { --accent: var(--red); }

  .card__wave {
    position: absolute;
    inset: 0;
    width: 100%;
    height: 100%;
  }
  .card__wave .wave-fill { fill: var(--accent); }

  .brand {
    position: absolute;
    display: flex;
    align-items: center;
    font-family: "Montserrat", sans-serif;
    font-weight: 600;
    color: var(--ink);
    white-space: nowrap;
  }
  .brand--stacked {
    left: 38px;
    top: 92px;
    gap: 14px;
    font-size: 34px;
    line-height: 1.1;
  }
  .brand--stacked .brand__mark {
    width: 22px;
    height: 120px;
    background: var(--ink);
    flex: none;
  }
  .brand--inline {
    left: 30px;
    top: 150px;
    gap: 12px;
    font-size: 22px;
    line-height: 1.15;
  }
  .brand--inline .brand__mark {
    width: 40px;
    height: 40px;
    border-radius: 50%;
    background: var(--accent);
    flex: none;
  }
</style>
</head>
<body>
<main class="sheet">

  <section class="card card--top-left card--green">
    <svg class="card__wave" viewBox="0 0 580 352" aria-hidden="true">
      <defs>
        <linearGradient id="silver-a" x1="0" y1="0" x2="1" y2="0">
          <stop offset="0" stop-color="var(--silver-light)"/>
          <stop offset="0.5" stop-color="var(--silver-mid)"/>
          <stop offset="1" stop-color="var(--silver-dark)"/>
        </linearGradient>
      </defs>
      <path fill="url(#silver-a)" d="M412 0 C378 46 312 112 302 200 C296 262 304 318 320 352 L580 352 L580 0 Z"/>
      <path class="wave-fill" d="M432 0 C400 46 334 114 324 204 C318 264 324 318 340 352 L580 352 L580 0 Z"/>
    </svg>
    <div class="brand brand--stacked">
      <span class="brand__mark"></span>
      <span class="brand__name">Vortig<br>Plumbing<br>&amp; Gas</span>
    </div>
  </section>

  <section class="card card--top-right card--red">
    <svg class="card__wave" viewBox="0 0 580 352" aria-hidden="true">
      <defs>
        <linearGradient id="silver-b" x1="0" y1="0" x2="1" y2="0">
          <stop offset="0" stop-color="var(--silver-light)"/>
          <stop offset="0.5" stop-color="var(--silver-mid)"/>
          <stop offset="1" stop-color="var(--silver-dark)"/>
        </linearGradient>
      </defs>
      <path fill="url(#silver-b)" d="M412 0 C378 46 312 112 302 200 C296 262 304 318 320 352 L580 352 L580 0 Z"/>
      <path class="wave-fill" d="M432 0 C400 46 334 114 324 204 C318 264 324 318 340 352 L580 352 L580 0 Z"/>
    </svg>
    <div class="brand brand--stacked">
      <span class="brand__mark"></span>
      <span class="brand__name">Vortig<br>Plumbing<br>&amp; Gas</span>
    </div>
  </section>

  <section class="card card--bottom-left card--green">
    <svg class="card__wave" viewBox="0 0 580 352" aria-hidden="true">
      <defs>
        <linearGradient id="silver-c" x1="0" y1="0" x2="1" y2="0">
          <stop offset="0" stop-color="var(--silver-light)"/>
          <stop offset="0.5" stop-color="var(--silver-mid)"/>
          <stop offset="1" stop-color="var(--silver-dark)"/>
        </linearGradient>
      </defs>
      <path fill="url(#silver-c)" d="M412 0 C378 46 312 112 302 200 C296 262 304 318 320 352 L580 352 L580 0 Z"/>
      <path class="wave-fill" d="M432 0 C400 46 334 114 324 204 C318 264 324 318 340 352 L580 352 L580 0 Z"/>
    </svg>
    <div class="brand brand--inline">
      <span class="brand__mark"></span>
      <span class="brand__name">Vortig<br>Plumbing &amp; Gas</span>
    </div>
  </section>

  <section class="card card--bottom-right card--red">
    <svg class="card__wave" viewBox="0 0 580 352" aria-hidden="true">
      <defs>
        <linearGradient id="silver-d" x1="0" y1="0" x2="1" y2="0">
          <stop offset="0" stop-color="var(--silver-light)"/>
          <stop offset="0.5" stop-color="var(--silver-mid)"/>
          <stop offset="1" stop-color="var(--silver-dark)"/>
        </linearGradient>
      </defs>
      <path fill="url(#silver-d)" d="M412 0 C378 46 312 112 302 200 C296 262 304 318 320 352 L580 352 L580 0 Z"/>
      <path class="wave-fill" d="M432 0 C400 46 334 114 324 204 C318 264 324 318 340 352 L580 352 L580 0 Z"/>
    </svg>
    <div class="brand brand--inline">
      <span class="brand__mark"></span>
      <span class="brand__name">Vortig<br>Plumbing &amp; Gas</span>
    </div>
  </section>

</main>
</body>
</html>
```